Business Card Design

We need a business card to highlight our property maintenance company. we specialize in commercial and industrial property maintenance. services include landscaping snow and ice management. janitorial services. cleanroom services. parking lot maintenance.
Updates
I have narrowed down to two designs thank you waiting on some minor changes to both designs to choose.
Target Market(s)
facility managers/property managers
Industry/Entity Type
Property Maintenance
Contact Information for Business Card
47 Brimwell Rd.
Wrenfield, Ma. 01564
978-552-7314
Look and feel
Each slider illustrates characteristics of the customer's brand and the style your logo design should communicate.

```html
<!DOCTYPE html>
<html lang="en">
<head>
<meta charset="utf-8">
<title>Crestline Property Care – Business Card</title>
<link rel="stylesheet" href="https://fonts.googleapis.com/css2?family=Exo+2:wght@400;500;600&display=swap">
<style>
  :root {
    --backdrop: #1e1e1f;
    --card: #f4f4f4;
    --card-shade: #e2e2e2;
    --ink: #3a3a3c;
    --ink-soft: #5a5a5d;
    --accent: #f3c12c;
    --rule: #6b6b6e;
  }
  * { box-sizing: border-box; margin: 0; padding: 0; }
  html, body { width: 1200px; height: 754px; overflow: hidden; }
  body {
    background: var(--backdrop);
    font-family: "Exo 2", sans-serif;
    color: var(--ink);
    display: flex;
    align-items: center;
    justify-content: center;
    gap: 40px;
  }
  .card {
    position: relative;
    width: 540px;
    height: 330px;
    background: radial-gradient(ellipse at 55% 40%, #ffffff 0%, var(--card) 55%, var(--card-shade) 100%);
  }
  .brand {
    display: flex;
    align-items: center;
    gap: 10px;
  }
  .brand-dot {
    width: 26px; height: 26px;
    border-radius: 50%;
    background: var(--accent);
    flex: none;
  }
  .brand-name {
    font-size: 15px;
    font-weight: 600;
    color: var(--ink);
    line-height: 1.15;
    text-transform: uppercase;
    letter-spacing: 0.5px;
  }
  .brand-place {
    font-size: 11px;
    font-weight: 500;
    color: var(--ink-soft);
    letter-spacing: 0.5px;
    margin-top: 3px;
  }

  /* front */
  .front .identity {
    position: absolute;
    left: 200px; top: 56px;
  }
  .person-name {
    font-size: 19px;
    font-weight: 500;
    letter-spacing: 0.6px;
    text-transform: uppercase;
  }
  .person-role {
    font-size: 11px;
    letter-spacing: 1px;
    text-transform: uppercase;
    color: var(--ink-soft);
    margin-top: 2px;
  }
  .contact-list {
    list-style: none;
    margin-top: 22px;
  }
  .contact-list li {
    display: flex;
    align-items: center;
    gap: 8px;
    font-size: 13px;
    margin-bottom: 9px;
  }
  .icon { width: 14px; height: 14px; flex: none; }
  .front .divider {
    position: absolute;
    left: 240px; top: 228px;
    width: 250px;
    border-top: 1px solid var(--rule);
  }
  .front .address {
    position: absolute;
    left: 240px; top: 258px;
    display: flex; align-items: center; gap: 8px;
    font-size: 12.5px;
  }
  .front .brand {
    position: absolute;
    left: 34px; top: 214px;
  }

  /* back */
  .back { display: flex; align-items: center; justify-content: center; }
  .back .brand-name { font-size: 17px; }
</style>
</head>
<body>
  <section class="card front">
    <div class="identity">
      <h1 class="person-name">Daniel Whitcomb</h1>
      <p class="person-role">General Manager</p>
      <ul class="contact-list">
        <li>
          <svg class="icon" viewBox="0 0 14 14"><circle cx="7" cy="7" r="7" fill="var(--ink)"/><path d="M4.6 3.6l1.3 1.3-.7.9c.5 1 1.2 1.7 2.2 2.2l.9-.7 1.3 1.3-.8 1.1C6.6 9.4 4.6 7.4 3.5 4.4z" fill="#fff"/></svg>
          978-552-7314
        </li>
        <li>
          <svg class="icon" viewBox="0 0 14 14"><circle cx="7" cy="7" r="7" fill="var(--ink)"/><rect x="3.5" y="4.5" width="7" height="5" fill="none" stroke="#fff" stroke-width="1"/><path d="M3.5 4.5L7 7.3l3.5-2.8" fill="none" stroke="#fff" stroke-width="1"/></svg>
          office@crestlinepc.com
        </li>
        <li>
          <svg class="icon" viewBox="0 0 14 14"><circle cx="7" cy="7" r="7" fill="var(--ink)"/><circle cx="7" cy="7" r="3.8" fill="none" stroke="#fff" stroke-width="0.9"/><path d="M3.2 7h7.6M7 3.2c-1.6 2-1.6 5.6 0 7.6M7 3.2c1.6 2 1.6 5.6 0 7.6" fill="none" stroke="#fff" stroke-width="0.8"/></svg>
          www.crestlinepc.com
        </li>
      </ul>
    </div>

    <div class="divider"></div>
    <p class="address">
      <svg class="icon" viewBox="0 0 14 14"><circle cx="7" cy="7" r="7" fill="var(--ink)"/><path d="M7 3a2.4 2.4 0 0 0-2.4 2.4C4.6 7.3 7 10.8 7 10.8s2.4-3.5 2.4-5.4A2.4 2.4 0 0 0 7 3z" fill="#fff"/><circle cx="7" cy="5.4" r="0.9" fill="var(--ink)"/></svg>
      47 Brimwell Rd., Wrenfield, MA 01599
    </p>

    <div class="brand">
      <span class="brand-dot"></span>
      <div>
        <p class="brand-name">Crestline<br>Property Care</p>
        <p class="brand-place">Wrenfield, Ma</p>
      </div>
    </div>
  </section>

  <section class="card back">
    <div class="brand">
      <span class="brand-dot"></span>
      <div>
        <p class="brand-name">Crestline<br>Property Care</p>
        <p class="brand-place">Wrenfield, Ma</p>
      </div>
    </div>
  </section>
</body>
</html>
```